Labour Day banner showcasing 20% off site

Banner graphic promoting our Labour Day sale
Size: 2000px x 600px
- examples from other companies and their sale banners have been uploaded for inspiration. Labour day examples are for the United States's holiday and submissions should NOT be in their country colours.
- product images can be found at www.tallpinegreens.com

Target Market(s)

19+

Industry/Entity Type

Cannabis

Requirements
Must have
• Phrases:
- “Happy Labour Day”
- “20% off site wide sale*"
- "Coupon code: Harvest20"
- Underneath phrase the date of sale “September 3rd - 7th”
- In tiny print “*excludes all sale and bundled items”
- MUST BE 2000px x 600px
Nice to have
• - images of the products or bud we carry which can be found at www.tallpinegreens.com
- bold
Should not have
• - company logo
- the American flag, we are a Canadian company, colours and flag should all be Canadian

```html
<!DOCTYPE html>
<html lang="en">
<head>
<meta charset="utf-8">
<title>Happy Labour Day – 20% Off Site Wide Sale</title>
<link rel="stylesheet" href="https://fonts.googleapis.com/css2?family=Poppins:wght@500;600;700;800&display=swap">
<style>
  :root {
    --navy-deep: #0a2240;
    --navy-mid: #133a63;
    --navy-glow: #2563a0;
    --white: #ffffff;
    --red: #e3202c;
    --red-dark: #a3141c;
    --blue-bright: #1aa3f2;
    --blue-main: #1478dc;
    --blue-dark: #0b4fb0;
    --blue-tail: #1595ea;
    --bud-green: #6f8a2e;
    --bud-amber: #b07a2c;
  }
  * { margin: 0; padding: 0; box-sizing: border-box; }
  html, body { width: 1200px; height: 360px; overflow: hidden; background: var(--navy-deep); }
  .banner {
    position: relative;
    width: 1200px;
    height: 360px;
    overflow: hidden;
    font-family: "Poppins", sans-serif;
    color: var(--white);
    background:
      radial-gradient(ellipse 420px 200px at 50% 8%, var(--navy-glow) 0%, rgba(37,99,160,0) 100%),
      radial-gradient(ellipse 900px 420px at 50% 40%, var(--navy-mid) 0%, var(--navy-deep) 100%);
  }
  .balloons {
    position: absolute;
    top: 0;
    height: 360px;
  }
  .balloons--left {
    left: 0;
    width: 300px;
    background:
      radial-gradient(circle 70px at 70px 80px, rgba(227,32,44,.85), rgba(227,32,44,0)),
      radial-gradient(circle 60px at 170px 190px, rgba(227,32,44,.9), rgba(227,32,44,0)),
      radial-gradient(circle 55px at 60px 250px, rgba(240,240,244,.85), rgba(240,240,244,0)),
      radial-gradient(circle 60px at 160px 320px, rgba(227,32,44,.8), rgba(227,32,44,0)),
      radial-gradient(circle 40px at 110px 40px, rgba(240,240,244,.8), rgba(240,240,244,0)),
      radial-gradient(circle 50px at 20px 150px, rgba(227,32,44,.7), rgba(227,32,44,0));
  }
  .balloons--right {
    right: 0;
    width: 290px;
    background:
      radial-gradient(circle 60px at 230px 50px, rgba(240,240,244,.8), rgba(240,240,244,0)),
      radial-gradient(circle 55px at 180px 110px, rgba(227,32,44,.85), rgba(227,32,44,0)),
      radial-gradient(circle 65px at 240px 210px, rgba(240,240,244,.85), rgba(240,240,244,0)),
      radial-gradient(circle 60px at 130px 230px, rgba(227,32,44,.85), rgba(227,32,44,0)),
      radial-gradient(circle 60px at 200px 320px, rgba(227,32,44,.8), rgba(227,32,44,0)),
      radial-gradient(circle 50px at 90px 330px, rgba(240,240,244,.75), rgba(240,240,244,0));
  }
  .bud {
    position: absolute;
    border-radius: 48% 52% 45% 55% / 55% 45% 55% 45%;
    background: radial-gradient(ellipse at 45% 45%, var(--bud-green) 0%, #4c6620 55%, var(--bud-amber) 100%);
    opacity: .9;
  }
  .bud--left { left: 236px; top: 146px; width: 134px; height: 84px; }
  .bud--right { left: 848px; top: 132px; width: 126px; height: 102px; }

  .shapes { position: absolute; inset: 0; }

  .headline {
    position: absolute;
    left: 0; right: 0;
    top: 56px;
    text-align: center;
  }
  .headline__ribbon {
    display: inline-block;
    position: relative;
    width: 158px;
    height: 28px;
    line-height: 28px;
    font-size: 19px;
    font-weight: 600;
    letter-spacing: 5px;
    text-indent: 5px;
  }
  .headline__title {
    margin-top: 6px;
    font-size: 49px;
    font-weight: 800;
    letter-spacing: 1.5px;
    line-height: 1.1;
  }
  .offer__percent {
    position: absolute;
    left: 460px; top: 214px;
    display: flex;
    align-items: center;
  }
  .offer__number { font-size: 44px; font-weight: 800; line-height: 1; letter-spacing: -1px; }
  .offer__unit { display: flex; flex-direction: column; margin-left: 2px; line-height: .95; font-weight: 800; }
  .offer__unit span:first-child { font-size: 20px; }
  .offer__unit span:last-child { font-size: 16px; }
  .offer__label {
    position: absolute;
    left: 547px; top: 203px;
    font-size: 19px;
    font-weight: 700;
    transform: rotate(-4deg);
    transform-origin: left center;
  }
  .offer__label sup { font-size: 11px; }
  .offer__dates {
    position: absolute;
    left: 551px; top: 240px;
    font-size: 13px;
    font-weight: 700;
    transform: rotate(-4deg);
    transform-origin: left center;
  }
  .offer__dates sup { font-size: 8px; }
  .coupon {
    position: absolute;
    left: 700px; top: 214px;
    width: 94px;
    text-align: center;
  }
  .coupon__label { font-size: 8.5px; font-weight: 600; display: block; }
  .coupon__code { font-size: 14px; font-weight: 700; display: block; margin-top: 1px; }
  .fine-print {
    position: absolute;
    left: 752px; top: 342px;
    font-size: 8.5px;
    font-weight: 500;
  }
</style>
</head>
<body>
<main class="banner">
  <div class="balloons balloons--left" role="img" aria-label="Cluster of red, white and striped heart balloons with maple leaves and silver confetti"></div>
  <div class="balloons balloons--right" role="img" aria-label="Cluster of red, white and striped heart balloons with maple leaves and silver confetti"></div>
  <div class="bud bud--left" role="img" aria-label="Photo of a dried cannabis bud"></div>
  <div class="bud bud--right" role="img" aria-label="Photo of a dried cannabis bud"></div>

  <svg class="shapes" width="1200" height="360" viewBox="0 0 1200 360" aria-hidden="true">
    <!-- ribbon behind the greeting -->
    <polygon points="524,57 682,57 676,71 682,85 524,85 518,71" fill="var(--red-dark)"/>
    <polygon points="522,55 680,55 674,69 680,83 522,83 516,69" fill="var(--red)"/>
    <!-- offer frame -->
    <polyline points="490,190 490,154 707,154 707,276 640,276" fill="none" stroke="var(--white)" stroke-width="1.2"/>
    <line x1="490" y1="276" x2="500" y2="276" stroke="var(--white)" stroke-width="1.2"/>
    <!-- offer ribbon tail -->
    <polygon points="464,262 632,256 632,300 560,302 522,334 530,302 468,300" fill="var(--blue-tail)"/>
    <!-- main band -->
    <polygon points="535,196 716,172 716,232 535,258" fill="var(--blue-main)"/>
    <!-- date strip -->
    <polygon points="540,236 690,218 676,244 540,262" fill="var(--blue-dark)"/>
    <!-- percent box -->
    <polygon points="456,210 535,206 535,270 456,276" fill="var(--blue-bright)"/>
    <polygon points="456,276 535,270 535,282 456,288" fill="var(--blue-dark)"/>
    <!-- dashed accents -->
    <line x1="500" y1="201" x2="610" y2="186" stroke="var(--blue-bright)" stroke-width="1" stroke-dasharray="3 2"/>
    <line x1="620" y1="266" x2="700" y2="258" stroke="var(--blue-bright)" stroke-width="1" stroke-dasharray="3 2"/>
    <!-- coupon heart balloon -->
    <path d="M746,286 C716,266 698,248 700,226 C702,208 718,200 732,202 C740,204 744,208 746,214 C748,208 752,204 760,202 C774,200 790,208 792,226 C794,248 776,266 746,286 Z" fill="var(--red)"/>
    <polygon points="742,286 750,286 746,292" fill="var(--red-dark)"/>
    <path d="M746,292 C742,310 752,330 748,360" fill="none" stroke="var(--white)" stroke-width="1" opacity=".7"/>
  </svg>

  <header class="headline">
    <div class="headline__ribbon">HAPPY</div>
    <h1 class="headline__title">LABOUR DAY</h1>
  </header>

  <div class="offer__percent">
    <span class="offer__number">20</span>
    <span class="offer__unit"><span>%</span><span>OFF</span></span>
  </div>
  <div class="offer__label">SITE WIDE SALE<sup>*</sup></div>
  <div class="offer__dates">September 3<sup>rd</sup> - 7<sup>th</sup></div>

  <div class="coupon">
    <span class="coupon__label">Coupon code:</span>
    <span class="coupon__code">Harvest20</span>
  </div>

  <p class="fine-print">* Excludes all sale &amp; bundled items</p>
</main>
</body>
</html>
```